Business card design for new brand

We have recently rebranded and need a new business card template.

We are an insurance underwriting agency. All of our products are sold via other partner companies, so these are just to pass on our details to other organisations.

We would like to see designs that use the colour green (current stationary generally uses lime green (rgb 142,190,63) and forest green (0,154,79) to comply with our logo's colours. We are happy with other shades of green.

Business cards need to include our logo, as well as space for:
1. Full name
2. Qualifications (optional)
3. Title
4. Office number
5. Mobile number
6. Email address

Our logo is enclosed here.

```html
<!DOCTYPE html>
<html lang="en">
<head>
<meta charset="utf-8">
<title>Verdant Cover – Business Card</title>
<link href="https://fonts.googleapis.com/css2?family=Lato:wght@400;700&display=swap" rel="stylesheet">
<style>
  :root {
    --backdrop: #d9d9d9;
    --card-white: #e6e6e6;
    --lime: #8ebe3f;
    --forest: #009a4f;
    --deep-green: #16612f;
    --text-grey: #333333;
    --grad-top: #d6d63c;
    --grad-mid: #20995a;
    --grad-bottom: #237548;
  }
  * { margin: 0; padding: 0; box-sizing: border-box; }
  html, body {
    width: 1200px; height: 800px; overflow: hidden;
    background: var(--backdrop);
    font-family: "Lato", sans-serif;
  }
  .card {
    position: absolute;
    left: 320px;
    width: 560px;
    height: 320px;
    box-shadow: 0 6px 16px rgba(0,0,0,0.22);
  }
  .card--front {
    top: 60px;
    background: linear-gradient(to bottom, var(--grad-top) 0%, #a6c955 25%, var(--grad-mid) 55%, var(--grad-bottom) 100%);
    display: flex; align-items: center; justify-content: center;
  }
  .card--back {
    top: 420px;
    background: var(--card-white);
  }
  .brand {
    display: flex; align-items: center; gap: 12px;
    font-weight: 700;
  }
  .brand__square { width: 30px; height: 30px; }
  .brand--light { color: #ffffff; font-size: 34px; }
  .brand--light .brand__square { background: #ffffff; }
  .brand--dark {
    position: absolute; left: 36px; top: 40px;
    color: var(--deep-green); font-size: 30px;
  }
  .brand--dark .brand__square { background: var(--forest); width: 26px; height: 26px; }
  .person {
    position: absolute; left: 36px; top: 160px; right: 38px;
  }
  .person__name {
    color: var(--deep-green); font-weight: 700; font-size: 18px;
  }
  .person__title-row {
    display: flex; align-items: flex-end; gap: 8px; margin-top: 2px;
  }
  .person__title { color: var(--text-grey); font-size: 15px; white-space: nowrap; }
  .person__rule { flex: 1; height: 1px; background: var(--deep-green); margin-bottom: 4px; }
  .contacts {
    position: absolute; left: 36px; top: 228px;
    list-style: none; font-size: 13.5px; color: var(--text-grey);
  }
  .contacts li { display: flex; align-items: center; gap: 10px; height: 20px; }
  .contacts svg { width: 14px; height: 14px; fill: var(--lime); }
  .address {
    position: absolute; right: 38px; top: 228px;
    font-style: normal; text-align: right;
    font-size: 13.5px; line-height: 20px; color: var(--text-grey);
  }
</style>
</head>
<body>
  <section class="card card--front">
    <div class="brand brand--light">
      <span class="brand__square"></span>
      <span class="brand__name">Verdant Cover Pty Ltd</span>
    </div>
  </section>

  <section class="card card--back">
    <div class="brand brand--dark">
      <span class="brand__square"></span>
      <span class="brand__name">Verdant Cover Pty Ltd</span>
    </div>

    <div class="person">
      <div class="person__name">Liam Hartley, M.Ed.</div>
      <div class="person__title-row">
        <span class="person__title">Managing Director</span>
        <span class="person__rule"></span>
      </div>
    </div>

    <ul class="contacts">
      <li>
        <svg viewBox="0 0 24 24" aria-hidden="true"><path d="M6.6 10.8a15.1 15.1 0 0 0 6.6 6.6l2.2-2.2a1 1 0 0 1 1-.25 11.4 11.4 0 0 0 3.6.57 1 1 0 0 1 1 1V20a1 1 0 0 1-1 1A17 17 0 0 1 3 4a1 1 0 0 1 1-1h3.5a1 1 0 0 1 1 1c0 1.25.2 2.45.57 3.57a1 1 0 0 1-.25 1z"/></svg>
        <span>+61 (02) 8456 7012</span>
      </li>
      <li>
        <svg viewBox="0 0 24 24" aria-hidden="true"><path d="M7 1h10a2 2 0 0 1 2 2v18a2 2 0 0 1-2 2H7a2 2 0 0 1-2-2V3a2 2 0 0 1 2-2zm0 3v14h10V4zm5 15.5a1.2 1.2 0 1 0 0 2.4 1.2 1.2 0 0 0 0-2.4z"/></svg>
        <span>+61 (0) 412 583 260</span>
      </li>
      <li>
        <svg viewBox="0 0 24 24" aria-hidden="true"><path d="M2 5h20v14H2zm2 2v.4l8 5.4 8-5.4V7zm0 2.8V17h16V9.8l-8 5.4z"/></svg>
        <span>liam.hartley@verdantcover.au</span>
      </li>
    </ul>

    <address class="address">
      Level 14, Harbourview Tower 3,<br>
      48 Kessel Street,<br>
      Fernvale NSW 2031
    </address>
  </section>
</body>
</html>
```